Modern, colorful Webdesign for SunnyPawTots: kids yoga, kids music and kids books

We need a new website design! www.sunnypawtots.de
- I started working on my website by buying a theme. But I don´t like it. And I can not adjust it to my needs. I need a new Design that transports the style and feeling of my logo and my concept
- Sunny Paw Tots sells services and products in the 3 main areas: 1. Kids Yoga, 2. Kids Stories/Books, 3. Kids Music, Crafting is included in some of the products
- Our Concept: Our products stand out from other products in their fields by bringing these different areas together and unite them to provide even more positive effects on the child´s development. For example: A Book is not only a book! It comes with a song and crafting elements inside the book. A Live Yoga session is not only movement and meditation, it incorporates also music, dancing and crafting. A live music class also incorporates international songs and yoga elements.
- Markets: Germany and USA/UK
- Target groups: mothers, fathers, caregivers, families with kids (age 0-10), well educated with middle to high income
- Business target groups: preschools, elementary schools, small businesses (for events), kids TV and radio programs, book stores, crafting stores
- Look & feel of the website: modern, playful, colorful

Target Market(s)

caregivers, moms, dads, grandparents, day cares, schools,

Industry/Entity Type

kids yoga, kids music, kids books, crafting

Number of Pages Required

5+ page

Font styles to use
Sans Serif

Requirements
Must have
• video/picture slider, colorful icons, overview of all icons, grafic to explain the concept
Nice to have
• Bring icons with products together. Show an interesting way to explain the concept of the brand with the icons and the bear.

```html
<!DOCTYPE html>
<html lang="en">
<head>
<meta charset="utf-8">
<title>SunnyPawTots – Kids Yoga, Music & Stories</title>
<link href="https://fonts.googleapis.com/css2?family=Jost:wght@300;400;500&family=Poppins:wght@500;600&family=Allura&family=Roboto:wght@400;500&display=swap" rel="stylesheet">
<style>
:root{
  --blue:#4a6cf0;
  --pink:#e2407f;
  --purple:#8a3fd6;
  --grad:linear-gradient(90deg,#9bb4ff 0%,#c8b4f5 50%,#f6acd6 100%);
  --grad-text:linear-gradient(90deg,#2f6bf0 0%,#8b3ddb 50%,#ee3e84 100%);
  --ink:#1f1f1f;
  --text:#6f6f6f;
  --line:#c9c9c9;
  --grey-bg:#f4f4f4;
  --lilac-bg:#f4eefb;
  --dark:#1d1b1c;
}
*{margin:0;padding:0;box-sizing:border-box}
html,body{width:1200px;height:4000px;overflow:hidden;background:#fff}
body{position:relative;font-family:'Jost',sans-serif;color:var(--ink)}
.abs{position:absolute}
a{text-decoration:none;color:inherit}

/* nav */
.nav a{position:absolute;font-size:14px;font-weight:400}
.nav .l{color:var(--blue)}
.nav .r{color:var(--pink)}
.nav-rule{position:absolute;height:1px;background:rgba(120,120,120,.35)}
.brand{position:absolute;font-family:'Jost',sans-serif;font-weight:500;font-size:24px;color:var(--purple);display:flex;align-items:center;gap:8px;transform:translateX(-50%);white-space:nowrap}
.brand .dot{width:14px;height:14px;border-radius:50%;background:#f3a73a}

/* hero */
.hero{left:0;top:0;width:1200px;height:574px;background:linear-gradient(100deg,#d9d6d4 0%,#efe9e6 35%,#f6ebe8 65%,#e4d2da 100%)}
.hero-title{left:0;width:1200px;top:360px;text-align:center;font-family:'Allura',cursive;font-size:66px;background:var(--grad-text);-webkit-background-clip:text;background-clip:text;color:transparent}
.hero-sub{left:0;width:1200px;top:446px;text-align:center;font-family:'Roboto',sans-serif;font-size:13px;line-height:29px;color:#2b2b2b}
.scroll{left:0;width:1200px;top:530px;text-align:center;font-size:10px;letter-spacing:6px;color:rgba(255,255,255,.9)}
.slides{left:1177px;top:272px;width:3px}
.slides i{display:block;width:2px;height:22px;background:rgba(160,150,155,.6);margin-bottom:12px}

/* buttons */
.btn{position:absolute;background:var(--grad);border-radius:40px;display:flex;align-items:center;justify-content:center;color:#1e2a55;font-weight:500}

.script{position:absolute;font-family:'Allura',cursive;background:linear-gradient(90deg,#b9a2f5,#8fb0ff 60%,#d8a6ec);-webkit-background-clip:text;background-clip:text;color:transparent;opacity:.8;white-space:nowrap}
.h2{position:absolute;font-family:'Poppins',sans-serif;font-weight:600;color:var(--ink);white-space:nowrap}

/* about */
.about-box{left:144px;top:658px;width:911px;height:265px;border:1px solid var(--line);border-bottom:none}
.about-bottom{top:922px;height:1px;background:var(--line)}
.about-p{left:220px;width:760px;top:805px;text-align:center;font-size:18px;font-weight:300;line-height:34px;color:var(--text)}

/* why */
.why{left:0;top:1013px;width:1200px;height:570px;background:var(--grey-bg)}
.why-p{left:146px;top:1217px;width:380px;font-size:15px;font-weight:300;line-height:28.5px;color:var(--text)}
.photo{position:absolute}

/* services */
.services{left:0;top:1583px;width:1200px;height:613px;background:var(--lilac-bg)}
.card{position:absolute;top:1765px;width:281px;height:355px;text-align:center}
.card.c1{border:1px solid #6d96f0}
.card.c2{border:1px solid #c174d8}
.card.c3{border:1px solid #c56fd0}
.card svg{position:absolute;left:101px;top:20px}
.card h3{position:absolute;left:0;width:100%;font-family:'Poppins',sans-serif;font-weight:500;font-size:17px;color:var(--ink)}
.card p{position:absolute;left:18px;width:245px;font-size:13px;font-weight:300;line-height:25.5px;color:var(--text)}
.card .more{position:absolute;left:88px;width:104px;height:40px;border-radius:20px;font-size:11px;display:flex;align-items:center;justify-content:center;background:#fff}
.c1 .more{border:1px solid #6d96f0;color:var(--blue)}
.c2 .more{border:1px solid #c174d8;color:#b04ac5}
.c3 .more{border:1px solid #e46a9b;color:var(--pink)}

/* event */
.event-frame{left:458px;top:2229px;width:610px;height:351px;border:1px solid var(--line);border-left:none;border-bottom:none}
.event-p{left:523px;top:2449px;width:480px;font-size:18px;font-weight:300;line-height:34.5px;color:var(--text)}
.event-sign{left:523px;top:2574px;font-size:18px;font-weight:400;color:#4a4a4a}

/* schedule */
.row{position:absolute;left:133px;width:932px;height:193px;background:#fff;box-shadow:0 8px 28px rgba(0,0,0,.08)}
.date{position:absolute;left:0;top:0;width:222px;height:193px;background:var(--dark);color:#fff;font-family:'Poppins',sans-serif;font-weight:500;font-size:44px;line-height:58px;text-align:center;padding-top:38px}
.row .pic{position:absolute;left:222px;top:0;width:280px;height:193px}
.row h4{position:absolute;left:536px;top:22px;font-weight:500;font-size:18px;color:#8a8080;text-decoration:underline;text-underline-offset:4px}
.row .meta{position:absolute;left:536px;display:flex;align-items:center;gap:14px;font-size:19px;font-weight:400;color:#555}
.row .btn{left:707px;top:67px;width:200px;height:60px;font-size:18px}

/* footer */
.footer{left:0;top:3770px;width:1200px;height:230px;background:var(--dark)}
.copy{left:0;width:1200px;top:3948px;text-align:center;font-size:11px;color:#d8d8d8}
</style>
</head>
<body>

<!-- HERO -->
<section class="abs hero" role="img" aria-label="Photo of children sitting cross-legged doing yoga with hands raised in a bright room"></section>
<svg class="abs" style="left:0;top:540px" width="1200" height="40" viewBox="0 0 1200 40">
  <path d="M0 34 L540 34 C565 34 575 10 600 10 C625 10 635 34 660 34 L1200 34 L1200 40 L0 40 Z" fill="#fff"/>
  <rect x="591" y="12" width="18" height="26" rx="9" fill="none" stroke="#c9c9c9" stroke-width="1.5"/>
  <line x1="600" y1="18" x2="600" y2="24" stroke="#c9c9c9" stroke-width="1.5"/>
</svg>
<nav class="nav">
  <a class="l" style="left:136px;top:48px">Yoga</a>
  <a class="l" style="left:219px;top:48px">Stories</a>
  <a class="r" style="left:312px;top:48px">Our Concept</a>
  <div class="nav-rule" style="left:432px;top:58px;width:120px"></div>
  <div class="nav-rule" style="left:650px;top:58px;width:120px"></div>
  <a class="l" style="left:800px;top:48px">Music</a>
  <a class="r" style="left:888px;top:48px">Crafting</a>
  <a class="r" style="left:992px;top:48px">Contact Us</a>
</nav>
<div class="brand" style="left:600px;top:74px"><span class="dot"></span>SunnyPawTots</div>
<h1 class="abs hero-title" style="font-weight:400">Something wonderful is about to happen</h1>
<p class="abs hero-sub">Through yoga, storytelling and music, children grow and develop skills they will use<br>throughout their lives.</p>
<div class="abs scroll">SCROLL DOWN</div>
<div class="abs slides"><i></i><i></i><i></i></div>

<!-- ABOUT -->
<div class="abs about-box"></div>
<div class="abs about-bottom" style="left:144px;width:346px"></div>
<div class="abs about-bottom" style="left:706px;width:349px"></div>
<div class="script" style="left:430px;top:612px;font-size:120px">About Us</div>
<h2 class="h2" style="left:508px;top:696px;font-size:30px">Our Mission</h2>
<div class="abs" style="left:599px;top:755px;width:1px;height:38px;background:#555"></div>
<p class="abs about-p">Relax, improve concentration, be active and get strong, train balance. Accompany your children into a world full of self-love, with a lot of fun and full of seriousness.</p>
<a class="btn" style="left:498px;top:895px;width:200px;height:58px;font-size:16px">Know More</a>

<!-- WHY US -->
<section class="abs why"></section>
<div class="script" style="left:136px;top:1050px;font-size:130px">Why Us</div>
<h2 class="h2" style="left:138px;top:1136px;font-size:32px">Our Values</h2>
<p class="abs why-p">Lorem ipsum dolor sit amet, consectetur adipisicing elit, sed do eiusmod tempor incididunt ut labore et dolore magna aliqua. Ut enim ad minim veniam, quis nostrud exercitation ullamco laboris nisi ut aliquip ex ea commodo consequat. Duis aute irure dolor in reprehenderit in voluptate velit esse cillum dolore eu fugiat nulla pariatur.</p>
<a class="btn" style="left:146px;top:1440px;width:175px;height:53px;font-size:15px">Know More</a>
<div class="photo" style="left:613px;top:1124px;width:231px;height:347px;background:linear-gradient(160deg,#eef0f4,#c8d2e6 55%,#5f7fb8)" role="img" aria-label="Photo of a smiling girl in a blue sweater listening to music on headphones"></div>
<div class="photo" style="left:878px;top:1057px;width:322px;height:177px;background:linear-gradient(120deg,#2c3f88,#6d78c0 50%,#b9b0d4)" role="img" aria-label="Photo of a mother reading a bedtime story to two children in bed"></div>
<div class="photo" style="left:878px;top:1260px;width:322px;height:262px;background:linear-gradient(160deg,#dde2ea,#a9bad0 60%,#3d6fb5)" role="img" aria-label="Photo of girls doing a yoga lunge pose in a studio"></div>

<!-- SERVICES -->
<section class="abs services"></section>
<div class="script" style="left:482px;top:1600px;font-size:120px">Services</div>
<h2 class="h2" style="left:506px;top:1686px;font-size:32px">Our Services</h2>

<div class="card c1" style="left:149px">
  <svg width="78" height="78" viewBox="0 0 78 78"><defs><linearGradient id="ig" x1="0" x2="1"><stop offset="0" stop-color="#4a6cf0"/><stop offset="1" stop-color="#e2407f"/></linearGradient></defs><circle cx="39" cy="39" r="37" fill="#fff" stroke="url(#ig)" stroke-width="1.5"/><path d="M33 48 V28 L49 24 V44" fill="none" stroke="url(#ig)" stroke-width="2"/><circle cx="30" cy="48" r="4" fill="none" stroke="url(#ig)" stroke-width="2"/><circle cx="46" cy="44" r="4" fill="none" stroke="url(#ig)" stroke-width="2"/></svg>
  <h3 style="top:118px">Music</h3>
  <p style="top:150px">Lorem ipsum dolor sit amet, consectetur adipisicing elit, sed do eiusmod tempor incididunt ut labore et dolore magna aliqua. Ut enim ad minim veniam, quis nostrud</p>
  <a class="more" style="top:291px">Read More</a>
</div>
<div class="card c2" style="left:464px">
  <svg width="78" height="78" viewBox="0 0 78 78"><circle cx="39" cy="39" r="37" fill="#fff" stroke="url(#ig)" stroke-width="1.5"/><path d="M39 24 C45 30 45 40 39 48 C33 40 33 30 39 24 Z M39 48 C32 46 26 40 25 32 C31 34 36 40 39 48 Z M39 48 C46 46 52 40 53 32 C47 34 42 40 39 48 Z" fill="none" stroke="url(#ig)" stroke-width="1.8"/><path d="M25 54 H53" stroke="url(#ig)" stroke-width="1.8"/></svg>
  <h3 style="top:118px">Yoga</h3>
  <p style="top:150px">Lorem ipsum dolor sit amet, consectetur adipisicing elit, sed do eiusmod tempor incididunt ut labore et dolore magna aliqua. Ut enim ad minim veniam, quis nostrud</p>
  <a class="more" style="top:288px">Read More</a>
</div>
<div class="card c3" style="left:781px">
  <svg width="78" height="78" viewBox="0 0 78 78"><circle cx="39" cy="39" r="37" fill="#fff" stroke="url(#ig)" stroke-width="1.5"/><path d="M22 50 C30 46 35 46 39 50 C43 46 48 46 56 50 V38 C48 34 43 34 39 38 C35 34 30 34 22 38 Z M39 38 V50" fill="none" stroke="url(#ig)" stroke-width="1.8"/><path d="M33 28 L34 24 L35 28 L39 29 L35 30 L34 34 L33 30 L29 29 Z M45 22 L46 25 L49 26 L46 27 L45 30 L44 27 L41 26 L44 25 Z" fill="url(#ig)"/></svg>
  <h3 style="top:114px">Stories/Books</h3>
  <p style="top:154px">Lorem ipsum dolor sit amet, consectetur adipisicing elit, sed do eiusmod tempor incididunt ut labore et dolore magna aliqua. Ut enim ad minim veniam, quis nostrud</p>
  <a class="more" style="top:302px">Read More</a>
</div>

<!-- EVENTS -->
<div class="photo" style="left:0;top:2196px;width:458px;height:545px;background:linear-gradient(140deg,#4f8a2a,#a8722f 45%,#e0b27c 70%,#6bbf4a)" role="img" aria-label="Photo of a smiling girl with headphones using a tablet on the grass"></div>
<div class="abs event-frame"></div>
<div class="script" style="left:516px;top:2262px;font-size:110px">Events</div>
<h2 class="h2" style="left:523px;top:2352px;font-size:31px">Private Event</h2>
<p class="abs event-p">Bliss, tranquility, and peace already have a place within you. Lunara’s mission is to provide a peaceful and inspiring environment for the nourishment of</p>
<div class="abs event-sign">Private Event Sign Up !!</div>
<a class="btn" style="left:523px;top:2649px;width:199px;height:59px;font-size:18px">Sign Up</a>

<!-- SCHEDULE -->
<div class="script" style="left:478px;top:2748px;font-size:110px;opacity:.25;filter:grayscale(1)">Schedule</div>
<h2 class="h2" style="left:0;width:1200px;text-align:center;top:2826px;font-size:40px;font-weight:500">Schedule List</h2>

<div class="row" style="top:2941px">
  <div class="date">06<br>Jun</div>
  <div class="pic" style="background:linear-gradient(120deg,#3a2420,#b56a3a 50%,#5b2b20)" role="img" aria-label="Photo of a child with headphones looking up"></div>
  <h4>Yoga Classes</h4>
  <div class="meta" style="top:66px"><svg width="22" height="24" viewBox="0 0 22 24"><path d="M11 22 C11 22 4 14 4 9 A7 7 0 0 1 18 9 C18 14 11 22 11 22 Z" fill="none" stroke="#f0a9a0" stroke-width="1.6"/><circle cx="11" cy="9" r="2.5" fill="none" stroke="#f0a9a0" stroke-width="1.6"/></svg>sunnypawtots</div>
  <div class="meta" style="top:116px"><svg width="24" height="24" viewBox="0 0 24 24"><circle cx="12" cy="12" r="10" fill="none" stroke="#f0c090" stroke-width="1.6"/><path d="M12 6 V12 H16" fill="none" stroke="#f0c090" stroke-width="1.6"/></svg>6:00 P.M</div>
  <a class="btn">Book Now</a>
</div>

<div class="row" style="top:3175px">
  <div class="date">06<br>Jun</div>
  <div class="pic" style="background:linear-gradient(120deg,#6a2a1e,#c24a3a 45%,#e2d6cc)" role="img" aria-label="Photo of a child reading a colourful picture book"></div>
  <h4>Music Therapy</h4>
  <div class="meta" style="top:66px"><svg width="22" height="24" viewBox="0 0 22 24"><path d="M11 22 C11 22 4 14 4 9 A7 7 0 0 1 18 9 C18 14 11 22 11 22 Z" fill="none" stroke="#f0a9a0" stroke-width="1.6"/><circle cx="11" cy="9" r="2.5" fill="none" stroke="#f0a9a0" stroke-width="1.6"/></svg>sunnypawtots</div>
  <div class="meta" style="top:116px"><svg width="24" height="24" viewBox="0 0 24 24"><circle cx="12" cy="12" r="10" fill="none" stroke="#f0c090" stroke-width="1.6"/><path d="M12 6 V12 H16" fill="none" stroke="#f0c090" stroke-width="1.6"/></svg>6:00 P.M</div>
  <a class="btn">Book Now</a>
</div>

<div class="row" style="top:3416px">
  <div class="date">06<br>Jun</div>
  <div class="pic" style="background:linear-gradient(180deg,#8a5a3a,#c89a6a 55%,#2f6fc0)" role="img" aria-label="Photo of children meditating on yoga mats in a classroom"></div>
  <h4>Crafting</h4>
  <div class="meta" style="top:66px"><svg width="22" height="24" viewBox="0 0 22 24"><path d="M11 22 C11 22 4 14 4 9 A7 7 0 0 1 18 9 C18 14 11 22 11 22 Z" fill="none" stroke="#f0a9a0" stroke-width="1.6"/><circle cx="11" cy="9" r="2.5" fill="none" stroke="#f0a9a0" stroke-width="1.6"/></svg>sunnypawtots</div>
  <div class="meta" style="top:116px"><svg width="24" height="24" viewBox="0 0 24 24"><circle cx="12" cy="12" r="10" fill="none" stroke="#f0c090" stroke-width="1.6"/><path d="M12 6 V12 H16" fill="none" stroke="#f0c090" stroke-width="1.6"/></svg>6:00 P.M</div>
  <a class="btn">Book Now</a>
</div>

<a class="btn" style="left:500px;top:3666px;width:198px;height:57px;font-size:18px">View All</a>

<!-- FOOTER -->
<footer class="abs footer"></footer>
<nav class="nav">
  <a class="l" style="left:147px;top:3872px">Yoga</a>
  <a class="l" style="left:230px;top:3872px">Stories</a>
  <a class="r" style="left:324px;top:3872px">Our Concept</a>
  <a class="l" style="left:790px;top:3869px">Music</a>
  <a class="r" style="left:878px;top:3869px">Crafting</a>
  <a class="r" style="left:982px;top:3869px">Contact Us</a>
</nav>
<div class="brand" style="left:600px;top:3864px;color:#b98af0"><span class="dot"></span>SunnyPawTots</div>
<div class="abs copy">©copyright sunnypawtots.de 2022.All Rights Reserved</div>

</body>
</html>
```